Criação de Papelaria Profissional para Beleza
A empresa queria:
" Atendemos clientes adultos masculino, feminino, adolescentes para tratamentos estéticos diversos como acne, rejuvenescimento facial, redução de medidas faciais e corporais, depilação, tratamento de celulite, estrias, medicina capilar, laser, cicatrizes, manchas, melasma, pequenos vasos, poros dilatados, limpeza de pele "

```html
<!DOCTYPE html>
<html lang="pt-BR">
<head>
<meta charset="utf-8">
<title>Assinatura – Aurora Clínica Estética</title>
<link rel="stylesheet" href="https://fonts.googleapis.com/css2?family=Montserrat:wght@300;400;500&display=swap">
<style>
  :root {
    --teal: #1ea6a1;
    --teal-dark: #117f7b;
    --teal-deep: #0b6663;
    --ink: #3c3c3c;
    --ink-soft: #5a5a5a;
    --white: #ffffff;
  }
  * { margin: 0; padding: 0; box-sizing: border-box; }
  html, body { width: 1200px; height: 1200px; overflow: hidden; background: var(--white); }
  .canvas { position: relative; width: 1200px; height: 1200px; font-family: "Montserrat", sans-serif; color: var(--ink); }
  .signature-shapes { position: absolute; inset: 0; }
  .brand {
    position: absolute; left: 40px; top: 590px; width: 380px;
    text-align: center; color: var(--white);
    font-weight: 400; font-size: 34px; letter-spacing: 3px; line-height: 1.25;
    text-transform: uppercase;
  }
  .brand .brand-dot {
    display: inline-block; width: 14px; height: 14px; border-radius: 50%;
    background: var(--white); margin-right: 12px; vertical-align: middle;
  }
  .person-name { position: absolute; left: 463px; top: 552px; font-size: 31px; font-weight: 400; color: var(--ink); }
  .person-role { position: absolute; left: 463px; top: 590px; font-size: 20px; font-weight: 300; color: var(--ink-soft); }
  .contact { position: absolute; display: flex; align-items: flex-start; gap: 12px; font-size: 17px; font-weight: 400; color: var(--ink-soft); line-height: 1.3; white-space: nowrap; }
  .contact svg { flex: none; width: 22px; height: 22px; }
  .c-phone { left: 462px; top: 635px; }
  .c-mail  { left: 462px; top: 668px; }
  .c-blog  { left: 462px; top: 701px; }
  .c-social { left: 805px; top: 635px; }
  .c-address { left: 805px; top: 668px; }
</style>
</head>
<body>
<div class="canvas">
  <svg class="signature-shapes" viewBox="0 0 1200 1200" width="1200" height="1200" aria-hidden="true">
    <defs>
      <linearGradient id="greyPanel" x1="0" y1="0" x2="0" y2="1">
        <stop offset="0" stop-color="#ffffff"/>
        <stop offset="1" stop-color="#e3e4e5"/>
      </linearGradient>
      <linearGradient id="tealPanel" x1="0" y1="0" x2="1" y2="1">
        <stop offset="0" stop-color="#27b3ad"/>
        <stop offset="1" stop-color="#148d89"/>
      </linearGradient>
      <linearGradient id="band" x1="0" y1="0" x2="0" y2="1">
        <stop offset="0" stop-color="#1a9994"/>
        <stop offset="1" stop-color="#0b6663"/>
      </linearGradient>
    </defs>
    <path class="panel-info" d="M400 516 H1121 Q1181 516 1181 576 V772 H400 Z" fill="url(#greyPanel)" stroke="#d4d5d6" stroke-width="1"/>
    <path class="panel-brand" d="M79 516 H425 Q437 516 437 528 V772 H19 V576 Q19 516 79 516 Z" fill="url(#tealPanel)"/>
    <rect class="band-base" x="19" y="764" width="1162" height="24" fill="url(#band)"/>
    <rect class="band-line" x="437" y="768" width="744" height="2" fill="#bfe6e4"/>
    <rect class="band-edge" x="19" y="784" width="1162" height="4" fill="var(--teal-deep)"/>
  </svg>

  <div class="brand"><span class="brand-dot"></span>Aurora<br>Clínica Estética</div>

  <div class="person-name">Dra. Lívia Marano</div>
  <div class="person-role">Esteticista</div>

  <div class="contact c-phone">
    <svg viewBox="0 0 22 22"><circle cx="11" cy="11" r="10" fill="none" stroke="#555" stroke-width="1.6"/><path d="M7.5 6.5l2 0 1 2.5-1.3 1a6 6 0 0 0 2.8 2.8l1-1.3 2.5 1v2a1 1 0 0 1-1 1A8 8 0 0 1 6.5 7.5a1 1 0 0 1 1-1z" fill="#555"/></svg>
    <span>+ 55 (11)94000-2233</span>
  </div>
  <div class="contact c-mail">
    <svg viewBox="0 0 22 22"><circle cx="11" cy="11" r="10" fill="none" stroke="#555" stroke-width="1.6"/><rect x="6" y="7.5" width="10" height="7" fill="none" stroke="#555" stroke-width="1.4"/><path d="M6 7.5l5 4 5-4" fill="none" stroke="#555" stroke-width="1.4"/></svg>
    <span>liviamarano@exemplo.com</span>
  </div>
  <div class="contact c-blog">
    <svg viewBox="0 0 22 22"><circle cx="11" cy="11" r="10" fill="#555"/></svg>
    <span>liviamarano.exemplo.net</span>
  </div>
  <div class="contact c-social">
    <svg viewBox="0 0 22 22"><circle cx="11" cy="11" r="10" fill="none" stroke="#555" stroke-width="1.6"/></svg>
    <span>livia_marano</span>
  </div>
  <div class="contact c-address">
    <svg viewBox="0 0 22 22"><circle cx="11" cy="11" r="10" fill="none" stroke="#555" stroke-width="1.6"/><path d="M11 5.5a3.8 3.8 0 0 0-3.8 3.8c0 2.8 3.8 7 3.8 7s3.8-4.2 3.8-7A3.8 3.8 0 0 0 11 5.5z" fill="#555"/><circle cx="11" cy="9.3" r="1.4" fill="#fff"/></svg>
    <span>Av. Orquídeas 245, Beta Office<br>Torre Norte Sala 804<br>Barueri - SP CEP 06400000</span>
  </div>
</div>
</body>
</html>
```